Computer screen desktop background design for dentists orthodontic office PCs

We need a new design to use as the Windows desktop background picture for the PC workstations in a dentists orthodontic office.
The design should be vector graphics.
The aspect ratio should reflect the monitor size (Resolution: 1920x1200).
In the uploaded files you can find the logo, the fonts and the design of the business card.
The design should not be brighter than the Windows 10 background picture (monitor lifetime).

The office logo must be the dominating part of the design (see uploaded files).

You don't need to use the same fonts, but the used fonts have to be in harmony with the fonts used in the logo and the business card.
The colors used have to be in harmony with the logo.
All the text below must be on the design.
The logical text groups are separated by empty lines.

Kieferorthopädie Tannwiese

Dr. med. dent. Lukas Brenner
Fachzahnarzt für Kieferorthopädie (CH) (Important information!)

Please make something cool and modern that attracts the patient's attraction when seen on the monitor screen.

Target Market(s)

dentists orthodontic office

Industry/Entity Type

Computer

Font styles to use
Sans Serif

Colors

Designer to choose colors to be used in the design.

Requirements
Must have
• The design should be vector graphics.
• The aspect ratio should reflect the monitor size (Resolution: 1920x1200).
• In the uploaded files you can find the logo, the fonts and the design of the business card.
• The design should not be brighter than the Windows 10 background picture (monitor lifetime).
• The office logo must be the dominating part of the design (see uploaded files).
• You don't need to use the same fonts, but the used fonts have to be in harmony with the fonts used in the logo and the business card.
• The colors used have to be in harmony with the logo.
• All the text below must be on the design.
• The logical text groups are separated by empty lines.
• Kieferorthopädie Tannwiese
• Dr. med. dent. Lukas Brenner
• Fachzahnarzt für Kieferorthopädie (CH) (Important information!)
• Adobe Illustrator source files
Nice to have
• Please make something cool and modern that attracts the patient's attraction when seen on the monitor screen.
Should not have

```html
<!DOCTYPE html>
<html lang="de">
<head>
<meta charset="utf-8">
<title>Kieferorthopädie Tannwiese – Desktop Wallpaper</title>
<link rel="stylesheet" href="https://fonts.googleapis.com/css2?family=Rubik:wght@500;600&family=Rajdhani:wght@500;600&display=swap">
<style>
  :root {
    --page-bg: #2a2b2e;
    --paper-top: #f4f5f7;
    --paper-bottom: #dcdfe4;
    --navy: #2a1f5c;
    --blue: #0b6fb5;
    --blue-deep: #075a97;
    --white: #ffffff;
  }
  * { margin: 0; padding: 0; box-sizing: border-box; }
  html, body {
    width: 1200px;
    height: 1000px;
    overflow: hidden;
    background: var(--page-bg);
  }
  .wallpaper {
    position: absolute;
    left: 0;
    top: 125px;
    width: 1200px;
    height: 750px;
    overflow: hidden;
    background: linear-gradient(180deg, var(--paper-top) 0%, var(--paper-bottom) 100%);
  }
  .wallpaper__shapes {
    position: absolute;
    inset: 0;
  }
  .brand {
    position: absolute;
    left: 110px;
    top: 92px;
    display: flex;
    align-items: center;
    gap: 36px;
  }
  .brand__dot {
    width: 92px;
    height: 92px;
    border-radius: 50%;
    background: var(--navy);
  }
  .brand__name {
    font-family: "Rubik", sans-serif;
    font-weight: 600;
    font-size: 50px;
    color: var(--navy);
    letter-spacing: 0.2px;
  }
  .doctor {
    position: absolute;
    left: 458px;
    top: 520px;
    color: var(--white);
  }
  .doctor__name {
    font-family: "Rajdhani", sans-serif;
    font-weight: 600;
    font-size: 60px;
    line-height: 1;
  }
  .doctor__title {
    margin-top: 8px;
    font-family: "Rajdhani", sans-serif;
    font-weight: 500;
    font-size: 32px;
    line-height: 1.1;
    letter-spacing: 0.6px;
  }
</style>
</head>
<body>
  <main class="wallpaper">
    <svg class="wallpaper__shapes" width="1200" height="750" viewBox="0 0 1200 750" aria-hidden="true">
      <defs>
        <linearGradient id="blueField" x1="0" y1="0" x2="1" y2="1">
          <stop offset="0" stop-color="var(--blue)" style="stop-color:#0b6fb5"/>
          <stop offset="1" stop-color="var(--blue-deep)" style="stop-color:#075a97"/>
        </linearGradient>
      </defs>
      <path class="blue-field" d="M0,750 L0,650 C280,520 680,340 1200,300 L1200,750 Z" fill="url(#blueField)"/>
      <path class="navy-swoosh" d="M270,545 C560,360 880,262 1200,242 L1200,284 C880,302 580,390 270,545 Z" fill="#2a1f5c"/>
    </svg>

    <header class="brand">
      <span class="brand__dot"></span>
      <h1 class="brand__name">Kieferorthopädie Tannwiese</h1>
    </header>

    <section class="doctor">
      <p class="doctor__name">Dr. med. dent. Lukas Brenner</p>
      <p class="doctor__title">Fachzahnarzt für Kieferorthopädie (CH)</p>
    </section>
  </main>
</body>
</html>
```